Business card design only (Have Logo Online) Shoudl be quick and easy for designer

We would like to have a business card design that is in-line with our company logo. Final deliverables should include two EPS extension file. One for the front card design and the other the back-end design. Please also indicate the font style used.

Advisory Pebbles is a social enterprise that focuses on utilizing technology, unique methodologies and international partnerships to provide a one-stop location for economical and dependable IT-related solutions.

Target Market(s)

Micro, small and medium business owners.

Industry/Entity Type

Business

Requirements
Must have
• The business card should incorporate our company logo.
Nice to have
• A little web 2.0 style would be nice but I haven''t decided yet.

```html
<!DOCTYPE html>
<html lang="en">
<head>
<meta charset="utf-8">
<title>Advisory Pebbles – Business Card</title>
<link href="https://fonts.googleapis.com/css2?family=Jost:ital,wght@0,300;0,400;0,500;0,700;1,300;1,400&family=Oswald:wght@300;400;500&display=swap" rel="stylesheet">
<style>
  :root {
    --green: #53955a;
    --green-dark: #3f7a45;
    --green-light: #b9da8c;
    --green-pale: #c9e3a6;
    --ink: #111111;
    --white: #ffffff;
    --black: #000000;
    --page: #ffffff;
  }
  * { box-sizing: border-box; margin: 0; padding: 0; }
  html, body {
    width: 1200px;
    height: 857px;
    overflow: hidden;
    background: var(--page);
  }
  .sheet {
    position: relative;
    width: 1200px;
    height: 857px;
  }
  .card {
    position: absolute;
    width: 593px;
    height: 339px;
    border: 2px solid var(--black);
    overflow: hidden;
  }

  /* Front */
  .card--front {
    left: 37px;
    top: 71px;
    background: var(--white);
  }
  .brand-disc {
    position: absolute;
    left: 40px;
    top: 12px;
    width: 136px;
    height: 136px;
    border-radius: 50%;
    background: var(--green-pale);
  }
  .brand-name {
    position: absolute;
    left: 64px;
    top: 152px;
    font-family: "Jost", sans-serif;
    font-weight: 700;
    font-size: 34px;
    letter-spacing: 3px;
    line-height: 40px;
    color: var(--green-dark);
    text-transform: uppercase;
    white-space: nowrap;
  }
  .holder {
    position: absolute;
    left: 356px;
    top: 40px;
    padding-left: 18px;
    border-left: 4px solid var(--green-light);
  }
  .holder__name {
    font-family: "Oswald", sans-serif;
    font-weight: 400;
    font-size: 30px;
    line-height: 36px;
    color: var(--ink);
  }
  .holder__title {
    font-family: "Jost", sans-serif;
    font-weight: 400;
    font-size: 19px;
    letter-spacing: 1.5px;
    line-height: 22px;
    color: var(--green);
  }
  .address {
    position: absolute;
    left: 308px;
    top: 196px;
    font-family: "Jost", sans-serif;
    font-weight: 300;
    font-size: 19px;
    line-height: 26px;
    color: var(--ink);
    font-style: normal;
  }
  .contact-band {
    position: absolute;
    left: 0;
    right: 0;
    bottom: 0;
    height: 44px;
    background: var(--green);
    display: flex;
    align-items: center;
    padding-left: 24px;
    font-family: "Jost", sans-serif;
    font-weight: 300;
    font-size: 19px;
    color: var(--white);
    white-space: nowrap;
  }
  .contact-band__label {
    font-family: "Oswald", sans-serif;
    font-weight: 400;
    color: var(--green-light);
    margin-right: 6px;
  }
  .contact-band__sep {
    color: var(--green-light);
    margin: 0 8px;
    font-weight: 500;
  }

  /* Back */
  .card--back {
    left: 573px;
    top: 440px;
    background: var(--green);
  }
  .back-disc {
    position: absolute;
    right: -40px;
    top: 10px;
    width: 220px;
    height: 220px;
    border-radius: 50%;
    background: var(--white);
    opacity: 0.05;
  }
  .slogan {
    position: absolute;
    left: 35px;
    top: 86px;
    font-family: "Jost", sans-serif;
    font-weight: 300;
    font-size: 48px;
    line-height: 52px;
    color: var(--white);
    white-space: nowrap;
  }
  .slogan em {
    font-style: italic;
    color: var(--green-light);
  }
  .promise {
    position: absolute;
    font-size: 22px;
    line-height: 28px;
    white-space: nowrap;
    color: var(--white);
  }
  .promise--one { left: 135px; top: 146px; }
  .promise--two { left: 159px; top: 179px; }
  .promise--three { right: 52px; top: 222px; }
  .cond {
    font-family: "Oswald", sans-serif;
    font-weight: 300;
    color: var(--green-light);
  }
  .cond--bold {
    font-weight: 500;
    color: var(--white);
  }
  .sans {
    font-family: "Jost", sans-serif;
    font-weight: 400;
  }
  .sans--strong { font-weight: 500; }
  .sans--italic { font-style: italic; }
  .web-band {
    position: absolute;
    left: 0;
    right: 0;
    bottom: 0;
    height: 49px;
    background: var(--black);
    border-top: 2px solid var(--white);
    display: flex;
    align-items: center;
    justify-content: center;
    font-family: "Oswald", sans-serif;
    font-weight: 400;
    font-size: 22px;
    color: var(--white);
  }
</style>
</head>
<body>
<main class="sheet">

  <section class="card card--front" aria-label="Card front">
    <div class="brand-disc" aria-hidden="true"></div>
    <div class="brand-name">Advisory Pebbles</div>

    <div class="holder">
      <p class="holder__name">Rowan Tesler</p>
      <p class="holder__title">FOUNDER</p>
    </div>

    <address class="address">
      1420 Alder Street<br>
      BC Canada<br>
      V5R 2K9
    </address>

    <div class="contact-band">
      <span class="contact-band__label">CELL:</span>1-604-555-0148
      <span class="contact-band__sep">|</span>
      <span class="contact-band__label">E-MAIL:</span>rowan.tesler@advisorypebbles.com
    </div>
  </section>

  <section class="card card--back" aria-label="Card back">
    <div class="back-disc" aria-hidden="true"></div>
    <h1 class="slogan">ROOTED <em>IN</em> TRUST</h1>
    <p class="promise promise--one">
      <span class="cond">Offering</span>
      <span class="cond cond--bold">practical,</span>
      <span class="sans">clear</span>
    </p>
    <p class="promise promise--two">
      <span class="cond">and</span>
      <span class="sans sans--strong">dependable</span>
      <span class="sans sans--italic">answers…</span>
    </p>
    <p class="promise promise--three">
      <span class="cond cond--bold">...not</span>
      <span class="cond">excuses.</span>
    </p>
    <div class="web-band">www.advisorypebbles.com</div>
  </section>

</main>
</body>
</html>
```